依頼詳細
写真・ビデオの撮影・編集および写真スタジオを行っています。お客様にお送りする封筒のデザインをお願いします。かっこよく・爽やかなイメージでお願いします。封筒の下位置部分のレイアウトでお願いします。。
記載項目
法人名/住所/電話/Fax/ホームページアドレス+ロゴ
希望イメージ
シンプル 複雑
単色 カラフル
暗い 明るい
日常 高級
遊び心 厳粛
未来的 伝統的
女性的 男性的
希望する色
青系、水色系、緑系
納品ファイル
• フォトショップ形式 (.psd)
補足説明
素材のロゴデータのロゴ部分と文字部分のバランスはおまかせ致します。
封筒の色は白色で考えております。よろしくお願い致します。

```html
<!DOCTYPE html>
<html lang="ja">
<head>
<meta charset="utf-8">
<title>株式会社LUMINA+ 封筒デザイン</title>
<link href="https://fonts.googleapis.com/css2?family=Noto+Sans+JP:wght@400;500;700&display=swap" rel="stylesheet">
<style>
  :root {
    --paper: #ffffff;
    --outline: #9aa3ad;
    --brand-blue: #1d5a8e;
    --ink: #1f2733;
    --on-blue: #ffffff;
  }
  * { margin: 0; padding: 0; box-sizing: border-box; }
  html, body { width: 778px; height: 1200px; overflow: hidden; background: var(--paper); }
  .envelope {
    position: relative;
    width: 778px;
    height: 1200px;
    font-family: "Noto Sans JP", sans-serif;
    color: var(--ink);
  }
  .envelope-art { position: absolute; inset: 0; }
  .flap-name {
    position: absolute;
    top: 22px;
    left: 0;
    width: 100%;
    text-align: center;
    font-size: 22px;
    font-weight: 700;
    color: var(--brand-blue);
    transform: rotate(180deg);
    letter-spacing: 0.02em;
  }
  .brand {
    position: absolute;
    left: 38px;
    top: 1014px;
    display: flex;
    align-items: center;
    gap: 12px;
  }
  .brand-name {
    font-size: 25px;
    font-weight: 700;
    color: var(--ink);
    letter-spacing: 0.01em;
  }
  .brand-square {
    width: 26px;
    height: 26px;
    background: var(--ink);
  }
  .sender {
    position: absolute;
    left: 446px;
    top: 1012px;
    color: var(--on-blue);
  }
  .sender-name {
    font-size: 25px;
    font-weight: 700;
    line-height: 1.3;
    margin-bottom: 8px;
    letter-spacing: 0.02em;
  }
  .sender-details {
    list-style: none;
    font-size: 17px;
    font-weight: 500;
    line-height: 1.36;
  }
</style>
</head>
<body>
<div class="envelope">
  <svg class="envelope-art" width="778" height="1200" viewBox="0 0 778 1200" aria-hidden="true">
    <path d="M8 1192 L8 118 L22 8 L756 8 L770 118 L770 1192 Z" fill="var(--paper)" stroke="var(--outline)" stroke-width="2"/>
    <line x1="8" y1="118" x2="770" y2="118" stroke="var(--outline)" stroke-width="2"/>
    <path d="M8 1096 C 200 1100, 330 1060, 430 1000 C 540 940, 670 936, 770 948 L770 1192 L8 1192 Z" fill="var(--brand-blue)"/>
    <path d="M8 1104 C 200 1108, 330 1068, 430 1008 C 540 948, 670 944, 770 956" fill="none" stroke="var(--paper)" stroke-width="2.5"/>
  </svg>

  <p class="flap-name">株式会社LUMINA+</p>

  <div class="brand">
    <span class="brand-name">株式会社LUMINA+</span>
    <span class="brand-square"></span>
  </div>

  <div class="sender">
    <p class="sender-name">株式会社ルミナプラス</p>
    <ul class="sender-details">
      <li>〒123-456</li>
      <li>○○○県○○市○○町1-2-3</li>
      <li>Tel.000-000-0000</li>
      <li>Fax.000-000-0000</li>
      <li>URL https://www.lumina-plus.example</li>
    </ul>
  </div>
</div>
</body>
</html>
```